Quillstone Business Card

We need a business card design. We have a logo from a previous Sketchfold project and I am attaching the logo files in jpeg and photoshop.

```html
<!DOCTYPE html>
<html lang="en">
<head>
<meta charset="UTF-8">
<title>Quillstone Business Card</title>
<link href="https://fonts.googleapis.com/css2?family=Open+Sans:wght@300;400;600;700;800&display=swap" rel="stylesheet">
<style>
  :root {
    --backdrop: #a9a9a9;
    --card: #434343;
    --white: #ffffff;
    --soft: #e4e4e4;
    --green: #4cc417;
  }
  * { margin: 0; padding: 0; box-sizing: border-box; }
  html, body { width: 1200px; height: 896px; overflow: hidden; }
  body {
    background: var(--backdrop);
    font-family: "Open Sans", Arial, sans-serif;
    position: relative;
  }
  .card {
    position: absolute;
    left: 250px;
    width: 700px;
    height: 400px;
    background: var(--card);
    overflow: hidden;
  }
  .card--front { top: 28px; }
  .card--back { top: 468px; }

  .brand {
    position: absolute;
    display: flex;
    align-items: center;
    gap: 16px;
  }
  .brand__square {
    width: 42px;
    height: 42px;
    background: var(--green);
  }
  .brand__name {
    font-weight: 800;
    font-size: 58px;
    line-height: 1;
    letter-spacing: -1px;
    color: var(--white);
  }
  .card--front .brand { left: 96px; top: 74px; }
  .card--back .brand { left: 50%; top: 128px; transform: translateX(-50%); }

  .accent-band {
    position: absolute;
    left: 0;
    top: 176px;
    width: 96px;
    height: 62px;
    background: var(--green);
  }
  .person {
    position: absolute;
    left: 112px;
    top: 180px;
    color: var(--white);
  }
  .person__name {
    font-weight: 700;
    font-size: 34px;
    line-height: 1.1;
    letter-spacing: 1px;
  }
  .person__role {
    font-weight: 300;
    font-size: 16px;
    letter-spacing: 7px;
    color: var(--soft);
    margin-top: 2px;
  }

  .contacts {
    position: absolute;
    left: 452px;
    top: 252px;
    list-style: none;
    color: var(--white);
    font-weight: 700;
    font-size: 15px;
    line-height: 1.3;
  }
  .contacts li {
    display: flex;
    align-items: flex-start;
    gap: 12px;
    margin-bottom: 7px;
  }
  .contacts svg {
    width: 18px;
    height: 18px;
    flex: none;
    fill: var(--green);
    margin-top: 1px;
  }

  .socials {
    position: absolute;
    left: 110px;
    top: 296px;
    display: flex;
    gap: 120px;
    list-style: none;
  }
  .socials li {
    display: flex;
    align-items: center;
    gap: 10px;
    color: var(--soft);
    font-size: 14px;
  }
  .socials__mark {
    width: 22px;
    height: 22px;
    background: var(--green);
  }
  .edge-tab {
    position: absolute;
    right: 0;
    top: 286px;
    width: 28px;
    height: 60px;
    background: var(--green);
  }
</style>
</head>
<body>

<section class="card card--front" aria-label="Card front">
  <div class="brand">
    <span class="brand__square"></span>
    <span class="brand__name">Quillstone</span>
  </div>
  <span class="accent-band"></span>
  <div class="person">
    <p class="person__name">DANIEL HARWOOD</p>
    <p class="person__role">GENERAL MANAGER</p>
  </div>
  <ul class="contacts">
    <li>
      <svg viewBox="0 0 24 24" aria-hidden="true"><path d="M12 3 2 12h3v9h5v-6h4v6h5v-9h3z"/></svg>
      <span>27 9th floor Plaza<br>Harbour Lane PLT</span>
    </li>
    <li>
      <svg viewBox="0 0 24 24" aria-hidden="true"><path d="M12 2a10 10 0 1 0 0 20 10 10 0 0 0 0-20zm7.9 9h-3.4a15 15 0 0 0-1.3-6.1A8 8 0 0 1 19.9 11zM12 4.1c.9 1.2 2.3 3.7 2.5 6.9h-5c.2-3.2 1.6-5.7 2.5-6.9zM8.8 4.9A15 15 0 0 0 7.5 11H4.1a8 8 0 0 1 4.7-6.1zM4.1 13h3.4a15 15 0 0 0 1.3 6.1A8 8 0 0 1 4.1 13zm7.9 6.9c-.9-1.2-2.3-3.7-2.5-6.9h5c-.2 3.2-1.6 5.7-2.5 6.9zm3.2-.8a15 15 0 0 0 1.3-6.1h3.4a8 8 0 0 1-4.7 6.1z"/></svg>
      <span>www.yourwebsite.com</span>
    </li>
    <li>
      <svg viewBox="0 0 24 24" aria-hidden="true"><path d="M2 5h20v14H2zm2 2v.5l8 5.5 8-5.5V7z"/></svg>
      <span>yourname@email.com</span>
    </li>
    <li>
      <svg viewBox="0 0 24 24" aria-hidden="true"><path d="M6.6 10.8a15 15 0 0 0 6.6 6.6l2.2-2.2c.3-.3.7-.4 1-.2 1.1.4 2.3.6 3.6.6.6 0 1 .4 1 1V20c0 .6-.4 1-1 1A17 17 0 0 1 3 4c0-.6.4-1 1-1h3.5c.6 0 1 .4 1 1 0 1.3.2 2.5.6 3.6.1.3 0 .7-.2 1z"/></svg>
      <span>012 345 6789</span>
    </li>
  </ul>
</section>

<section class="card card--back" aria-label="Card back">
  <div class="brand">
    <span class="brand__square"></span>
    <span class="brand__name">Quillstone</span>
  </div>
  <ul class="socials">
    <li><span class="socials__mark"></span>yourname</li>
    <li><span class="socials__mark"></span>@yourname</li>
    <li><span class="socials__mark"></span>yourname</li>
  </ul>
  <span class="edge-tab"></span>
</section>

</body>
</html>
```